依頼概要
〇依頼の目的/概要
電子書籍(lumora)の表紙デザインをおねがいします。

〇画像サイズ
表紙サイズの理想的な寸法は2560×1600ピクセルです。
注:画像の寸法は1000×625ピクセル以上であることが必要です。
画像の最大の寸法は10000×10000ピクセルです。

〇タイトル
夜更けの庭で青い灯をさがす旅の物語です!

〇帯キャッチ

・眠ることも許されない
死にたくなるようなかゆみと痛みから
柔らかい潤いのある肌になった

・人生の波と家族とのご縁をひもといて
薬を使わずに治す

・「絶対に治る、治ったら
同じように苦しんでいる人の為に役立つ本を書こう」
・・・と決めていました。

デザイナーさんの判断で、
どれかを使ってもらっても、
または全部を使ってもらってもOKです。

〇著者 ぽんたるべカフェ 占導師 千景(柴崎奈緒)

文字の大きさと配置と色のインパクトがあって一目惚れしました。
修正依頼にも迅速な対応もありがたかったです。

初めての電子書籍の執筆と初めてのワークベリーへの仕事依頼で、
ドキドキで、いろいろ小さなわからないところだらけでした。
たくさんの提案、どれも素敵なものばかりですべての提案者の方々に
感謝の氣持ちでいっぱいです。ありがとうございました。
これからもアトピー性皮膚炎を克服するための電子書籍を執筆していく予定なので
また、協力していただけたら嬉しいです。

```html
<!DOCTYPE html>
<html lang="ja">
<head>
<meta charset="utf-8">
<title>夜更けの庭で青い灯をさがす旅の物語です!</title>
<link rel="stylesheet" href="https://fonts.googleapis.com/css2?family=Noto+Sans+JP:wght@400;500;700;900&display=swap">
<style>
  :root {
    --paper: #ffffff;
    --ink: #1a1a1a;
    --accent-orange: #f0a22a;
    --band-purple: #8c7aa6;
    --catch-purple: #7b5f98;
    --author-mauve: #8a5a86;
    --figure-tone-a: #f4eef4;
    --figure-tone-b: #e3d9e8;
  }
  html, body {
    margin: 0;
    padding: 0;
    width: 750px;
    height: 1200px;
    overflow: hidden;
    background: var(--paper);
  }
  .cover {
    position: relative;
    width: 750px;
    height: 1200px;
    background: var(--paper);
    font-family: "Noto Sans JP", sans-serif;
    overflow: hidden;
  }
  .title-column {
    position: absolute;
    top: 70px;
    writing-mode: vertical-rl;
    font-weight: 900;
    font-size: 70px;
    line-height: 1;
    letter-spacing: 0;
    color: var(--ink);
    margin: 0;
  }
  .title-column.c1 { left: 580px; }
  .title-column.c2 { left: 485px; }
  .title-column.c3 { left: 390px; }
  .title-column.c4 { left: 295px; }
  .cross-mark {
    position: absolute;
    left: 405px;
    top: 195px;
    width: 290px;
    height: 300px;
  }
  .author-affiliation {
    position: absolute;
    left: 92px;
    top: 320px;
    writing-mode: vertical-rl;
    font-size: 22px;
    font-weight: 500;
    color: var(--ink);
    letter-spacing: 2px;
  }
  .author-name {
    position: absolute;
    writing-mode: vertical-rl;
    font-size: 54px;
    font-weight: 500;
    color: var(--author-mauve);
    line-height: 1;
  }
  .author-name.surname { left: 118px; top: 580px; }
  .author-name.given { left: 172px; top: 655px; }
  .figure-area {
    position: absolute;
    left: 380px;
    top: 500px;
    width: 360px;
    height: 305px;
    background: linear-gradient(180deg, var(--figure-tone-a), var(--figure-tone-b));
    border-radius: 160px 160px 0 0;
  }
  .catch-band {
    position: absolute;
    left: 0;
    top: 805px;
    width: 750px;
    height: 395px;
    background: var(--band-purple);
  }
  .catch-box {
    position: absolute;
    left: 25px;
    top: 33px;
    width: 640px;
    padding: 10px 0 14px 18px;
    box-sizing: border-box;
    background: var(--paper);
    color: var(--catch-purple);
    font-weight: 900;
    font-size: 68px;
    line-height: 1.08;
    letter-spacing: 1px;
  }
  .catch-lead {
    position: absolute;
    left: 28px;
    top: 205px;
    margin: 0;
    color: var(--paper);
    font-weight: 700;
    font-size: 33px;
    line-height: 1.4;
  }
</style>
</head>
<body>
  <main class="cover">
    <h1 class="title-block">
      <span class="title-column c1">夜更けの庭で</span>
      <span class="title-column c2">青い灯を</span>
      <span class="title-column c3">さがす旅の</span>
      <span class="title-column c4">物語です!</span>
    </h1>

    <svg class="cross-mark" viewBox="0 0 290 300" aria-hidden="true">
      <line x1="18" y1="18" x2="272" y2="282" stroke="var(--accent-orange)" stroke-width="30" stroke-linecap="round" opacity="0.95"/>
      <line x1="272" y1="18" x2="18" y2="282" stroke="var(--accent-orange)" stroke-width="30" stroke-linecap="round" opacity="0.95"/>
    </svg>

    <div class="author-affiliation">ぽんたるべカフェ 占導師</div>
    <div class="author-name surname">柴崎</div>
    <div class="author-name given">奈緒</div>

    <div class="figure-area" role="img" aria-label="頬に手を当てて悩む女性のイラスト"></div>

    <section class="catch-band">
      <div class="catch-box">眠ることも<br>許されない</div>
      <p class="catch-lead">死にたくなるようなかゆみと痛みから<br>柔らかい潤いのある肌になった</p>
    </section>
  </main>
</body>
</html>
```